Pull Up Banners

Would like to have these pull up banner designs changed to a new modern theme. I have running a sales booth and want to re-design the banner designs. I have uploaded old banner design, I need phone number and website added onto bottom. Happy to consider images to attract people attention to increase sales and spark people interest walking past.

```html
<!DOCTYPE html>
<html lang="en">
<head>
<meta charset="utf-8">
<title>Clearline Pull Up Banner</title>
<link href="https://fonts.googleapis.com/css2?family=Montserrat:wght@400;500;600;700&display=swap" rel="stylesheet">
<style>
  :root {
    --page-bg: #e4e4e4;
    --white: #ffffff;
    --orange-top: #e07b24;
    --orange-mid: #de6a1c;
    --orange-low: #e05a24;
    --orange-hot: #f05f0e;
    --brand-orange: #e8561a;
    --ink: #1f1d1e;
  }
  * { margin: 0; padding: 0; box-sizing: border-box; }
  html, body {
    width: 1141px; height: 1200px; overflow: hidden;
    background: var(--page-bg);
    font-family: "Montserrat", sans-serif;
  }
  .banner {
    position: absolute;
    left: 335px; top: 17px;
    width: 575px; height: 1425px;
    transform: scale(0.8175);
    transform-origin: top left;
    overflow: hidden;
    background: linear-gradient(160deg, var(--orange-top) 0%, var(--orange-mid) 45%, var(--orange-low) 80%, var(--orange-hot) 100%);
    color: var(--white);
  }
  .banner-shapes { position: absolute; inset: 0; }
  .brand {
    position: absolute; left: 52px; top: 58px;
    display: flex; align-items: center; gap: 18px;
  }
  .brand-dot {
    width: 62px; height: 62px; border-radius: 50%;
    background: var(--brand-orange);
  }
  .brand-text { display: flex; flex-direction: column; }
  .brand-name {
    font-weight: 600; font-size: 43px; letter-spacing: 2px;
    color: var(--brand-orange); line-height: 1;
  }
  .brand-tagline {
    font-weight: 600; font-size: 9.5px; letter-spacing: 1.6px;
    color: var(--ink); margin-top: 6px;
  }
  .headline {
    position: absolute; left: 50px; top: 374px;
    font-weight: 700; font-size: 49px; line-height: 60px;
    letter-spacing: 0.5px; text-transform: uppercase;
  }
  .headline-rule {
    position: absolute; left: 50px; top: 571px;
    width: 63px; height: 5px; background: var(--white);
  }
  .service { position: absolute; width: 190px; text-align: center; }
  .service-icon { display: block; width: 98px; height: 98px; margin: 0 auto; }
  .service-label { margin-top: 18px; font-size: 21px; font-weight: 400; line-height: 27px; }
  .service--voip { left: 30px; top: 636px; }
  .service--sms { left: 234px; top: 636px; }
  .service--teams { left: 30px; top: 858px; }
  .service--net { left: 234px; top: 858px; }
  .contact {
    position: absolute; left: 0; right: 0; top: 1298px;
    text-align: center; font-weight: 500;
  }
  .contact-phone { font-size: 37px; line-height: 46px; }
  .contact-web { font-size: 33px; line-height: 44px; }
</style>
</head>
<body>
  <div class="banner">
    <svg class="banner-shapes" viewBox="0 0 575 1425" aria-hidden="true">
      <path d="M0,0 H575 V222 C562,258 505,276 432,273 C255,266 85,185 0,68 Z" fill="#ffffff"/>
      <path d="M0,1075 C85,1195 250,1272 445,1273 C520,1273 565,1248 575,1218 L575,1425 L0,1425 Z" fill="#1f1d1e"/>
    </svg>

    <div class="brand">
      <span class="brand-dot"></span>
      <div class="brand-text">
        <span class="brand-name">CLEARLINE</span>
        <span class="brand-tagline">YOUR TRUSTED PARTNER FOR ALL THINGS I.T</span>
      </div>
    </div>

    <h1 class="headline">Cloud Phone<br>System &amp;<br>Internet</h1>
    <div class="headline-rule"></div>

    <div class="service service--voip">
      <svg class="service-icon" viewBox="0 0 98 98" fill="none" stroke="#fff">
        <circle cx="49" cy="49" r="47" stroke-width="2"/>
        <path d="M34 30 l8 -3 l6 12 l-5 5 c2 6 6 11 12 14 l5 -5 l12 6 l-3 8 c-20 2 -38 -16 -35 -37 z" fill="#fff" stroke="none"/>
        <path d="M52 31 a10 10 0 0 1 10 10 M52 23 a18 18 0 0 1 18 18 M52 15 a26 26 0 0 1 26 26" stroke-width="3" stroke-linecap="round"/>
      </svg>
      <p class="service-label">VoIP &amp; Phone<br>Systems</p>
    </div>

    <div class="service service--sms">
      <svg class="service-icon" viewBox="0 0 98 98" fill="none" stroke="#fff">
        <circle cx="49" cy="49" r="47" stroke-width="2"/>
        <rect x="22" y="27" width="54" height="38" rx="5" fill="#fff" stroke="none"/>
        <path d="M32 64 l4 10 l8 -10 z" fill="#fff" stroke="none"/>
        <path d="M29 37 H69 M29 45 H69 M29 53 H69" stroke="#e07024" stroke-width="3"/>
      </svg>
      <p class="service-label">SMS Gateway</p>
    </div>

    <div class="service service--teams">
      <svg class="service-icon" viewBox="0 0 98 98" fill="#fff" stroke="none">
        <circle cx="49" cy="49" r="47" fill="none" stroke="#fff" stroke-width="2"/>
        <circle cx="49" cy="33" r="8"/>
        <circle cx="30" cy="42" r="6"/>
        <circle cx="68" cy="42" r="6"/>
        <path d="M36 68 c0 -14 6 -22 13 -22 c7 0 13 8 13 22 z"/>
        <path d="M18 68 c0 -10 5 -17 12 -17 c3 0 5 1 6 2 c-3 4 -4 9 -4 15 z"/>
        <path d="M80 68 c0 -10 -5 -17 -12 -17 c-3 0 -5 1 -6 2 c3 4 4 9 4 15 z"/>
      </svg>
      <p class="service-label">Unified<br>Team Calling</p>
    </div>

    <div class="service service--net">
      <svg class="service-icon" viewBox="0 0 98 98" fill="none" stroke="#fff" stroke-linecap="round">
        <circle cx="49" cy="49" r="47" stroke-width="2"/>
        <path d="M22 40 a38 38 0 0 1 54 0" stroke-width="5"/>
        <path d="M31 50 a25 25 0 0 1 36 0" stroke-width="5"/>
        <path d="M40 59 a12 12 0 0 1 18 0" stroke-width="5"/>
        <circle cx="49" cy="70" r="5" fill="#fff" stroke="none"/>
      </svg>
      <p class="service-label">ADSL, Fibre &amp;<br>4G Internet</p>
    </div>

    <div class="contact">
      <p class="contact-phone">08-5550-1234</p>
      <p class="contact-web">clearlinecomputers.com.au</p>
    </div>
  </div>
</body>
</html>
```